Guaranteed Job - Sleek Sexy Business Card UV Spot

Im looking for a sleek and sexy business card, that resembles elite or VIP status status.
our business is corinvale.example
you can view our products on there, but our main audience for handing out our cards will be for people in the hospitality industry, so it will need to impress high management and CEO of hotels and restaurants, bars, clubs etc...
the card features will have UV spot on both sides, 400gsm stock. standard size.
Artwork should be 86 x 54mm + 2mm bleed = 90 x 58mm
it should have a nice "unique" uv spot pattern that highlights the card, not a repeated pattern, theres no originality there, and it will be disregarded.
The written material will be:
Corin Vale Hospitality College (logo)
Tobin Marsh
Director
Phone: 1300 615 737
Mobile: 0455 817 296
Email: info@corinvale.example
website: www.corinvale.example
I'm looking for originality here, i don't want just a simple stock card, want something that has a wow factor for people.
You will find the logo attached. you may invert the white to black words to suit the background as you please.
thank you and good luck
As a side note, ive received a lot of proposals, im too busy to give feedback to each and every one, so if i havent provided feedback for your design within 24 hours, then consider it not acceptable, and you could resubmit another design.
So far i have not seen any design that stood out for me, they all seem pretty generic. there nothing thats unique, i would figure for the amount that im offering, that people would put some more effort and creativity into the design.
so far over 200 designs submitted, and nothing i have seen looks very original, everything looks like a different variation of the same stuff, i said it very clearly i wanted something unique, the only thing that has come close to it so far is this one
Reason: Ive received alot of design concepts and i have reviewed everyone, but i havent had time to give feedback to every single one, only the ones that have interested me, if i havent responded, its because i havent found it good enough.
so far only a few design have been on par with what ive been looking for, an attractive eye popping design.
heres a few of them,
http://files.pixelbazaar.example/design_img/51736/62418/62418_2840915_51736_image.jpg
http://files.pixelbazaar.example/design_img/51736/68254/68254_2841377_51736_image.jpg
theyre, both unique and original, and eye catching, the only thing theyre missing is the sexyness.
if you still think you have some creativity left in your minds, then throw it on here.
Reason: Sorry guys for the delay, I was in a serious accident and out of commission for the past few months, I'm just slowly recovering now, please bare with me as i try to attend to this project, it may take me awhile as I have other projects that are on standby, I'm not 100% at the moment, so im extending the deadline for 2 weeks right now. Thanks for your patience.
Hospitality

```html
<!DOCTYPE html>
<html lang="en">
<head>
<meta charset="utf-8">
<title>Corin Vale Hospitality College – Business Card</title>
<link rel="stylesheet" href="https://fonts.googleapis.com/css2?family=Oswald:wght@500&family=Dosis:wght@500;600&display=swap">
<style>
  :root {
    --backdrop: #3b3b3d;
    --card-white: #ffffff;
    --ice-pale: #e8f3fc;
    --ice-light: #c4e1f6;
    --ice-mid: #9fcbee;
    --ice-deep: #6aaee0;
    --ice-shadow: #8db4cf;
    --brand-blue: #5b9fd8;
    --ink: #1e1e22;
    --muted: #7b7f86;
    --rule: #8fc0e8;
  }
  * { box-sizing: border-box; margin: 0; padding: 0; }
  html, body { width: 1200px; height: 848px; overflow: hidden; }
  body {
    background: var(--backdrop);
    display: flex;
    align-items: center;
    justify-content: center;
    gap: 40px;
    font-family: "Dosis", sans-serif;
  }
  .card {
    position: relative;
    width: 540px;
    height: 324px;
    overflow: hidden;
    background: linear-gradient(100deg, var(--card-white) 0%, var(--card-white) 28%, var(--ice-pale) 50%, var(--ice-light) 70%);
    box-shadow: 0 10px 24px rgba(0,0,0,.45);
  }
  /* Area reserved for the faceted crystal UV-spot artwork */
  .crystal-art {
    position: absolute;
    top: 0; right: 0;
    width: 320px; height: 100%;
    background:
      radial-gradient(circle at 78% 12%, rgba(255,255,255,.9) 0, rgba(255,255,255,0) 18%),
      radial-gradient(circle at 45% 30%, rgba(255,255,255,.55) 0, rgba(255,255,255,0) 16%),
      radial-gradient(circle at 60% 70%, rgba(255,255,255,.45) 0, rgba(255,255,255,0) 14%),
      radial-gradient(ellipse at 62% 55%, var(--ice-deep) 0, rgba(106,174,224,0) 60%),
      radial-gradient(ellipse at 90% 85%, var(--ice-shadow) 0, rgba(141,180,207,0) 45%),
      linear-gradient(90deg, rgba(196,225,246,0) 0%, var(--ice-mid) 40%, var(--ice-deep) 100%);
  }
  .wordmark {
    position: absolute;
    display: flex;
    align-items: center;
    gap: 12px;
  }
  .wordmark-square {
    width: 40px; height: 40px;
    background: var(--brand-blue);
    flex: none;
  }
  .wordmark-name {
    font-family: "Oswald", sans-serif;
    font-weight: 500;
    color: var(--ink);
    text-transform: uppercase;
    line-height: 1.05;
    font-size: 24px;
    letter-spacing: .5px;
  }
  .front .wordmark { left: 40px; top: 102px; }
  .back .wordmark { left: 40px; top: 26px; }

  .website {
    position: absolute;
    left: 40px; bottom: 28px;
    font-size: 26px;
    font-weight: 500;
    color: var(--brand-blue);
    letter-spacing: .5px;
  }
  .website-rule {
    position: absolute;
    left: 0; bottom: 20px;
    width: 330px; height: 1.5px;
    background: var(--rule);
  }

  .person {
    position: absolute;
    left: 40px; top: 118px;
  }
  .person-name {
    font-family: "Oswald", sans-serif;
    font-weight: 500;
    font-size: 30px;
    color: var(--brand-blue);
    text-transform: uppercase;
    line-height: 1;
  }
  .person-role {
    font-size: 18px;
    font-weight: 500;
    color: var(--muted);
    margin-top: 4px;
  }

  .contacts {
    position: absolute;
    left: 0; top: 202px;
    list-style: none;
  }
  .contact {
    display: flex;
    align-items: center;
    height: 30px;
    font-size: 20px;
    font-weight: 600;
    color: var(--ink);
    letter-spacing: .4px;
  }
  .contact-rule {
    width: 28px; height: 1.5px;
    background: var(--rule);
  }
  .contact-icon {
    width: 26px; height: 26px;
    margin-right: 10px;
    flex: none;
  }
</style>
</head>
<body>

  <section class="card front" aria-label="Card front">
    <div class="crystal-art" role="img" aria-label="Faceted pale blue crystal UV-spot artwork with light sparkles"></div>
    <div class="wordmark">
      <span class="wordmark-square"></span>
      <span class="wordmark-name">Corin Vale<br>Hospitality College</span>
    </div>
    <p class="website">www.corinvale.example</p>
    <span class="website-rule"></span>
  </section>

  <section class="card back" aria-label="Card back">
    <div class="crystal-art" role="img" aria-label="Faceted pale blue crystal UV-spot artwork with light sparkles"></div>
    <div class="wordmark">
      <span class="wordmark-square"></span>
      <span class="wordmark-name">Corin Vale<br>Hospitality College</span>
    </div>
    <div class="person">
      <h1 class="person-name">Tobin Marsh</h1>
      <p class="person-role">Director</p>
    </div>
    <ul class="contacts">
      <li class="contact">
        <span class="contact-rule"></span>
        <svg class="contact-icon" viewBox="0 0 26 26" aria-hidden="true">
          <circle cx="13" cy="13" r="11.5" fill="#eaf4fc" stroke="#8fc0e8" stroke-width="1.5"/>
          <path d="M9 7.5c-1 .6-1.6 1.6-1.2 3 .9 3 3.5 5.9 6.6 7 1.3.5 2.4 0 3-1l-2.2-2-1.3.8c-1.3-.6-2.5-1.9-3-3.2l.9-1.2z" fill="#5b9fd8"/>
        </svg>
        1300 615 737
      </li>
      <li class="contact">
        <span class="contact-rule"></span>
        <svg class="contact-icon" viewBox="0 0 26 26" aria-hidden="true">
          <circle cx="13" cy="13" r="11.5" fill="#eaf4fc" stroke="#8fc0e8" stroke-width="1.5"/>
          <rect x="9.5" y="6.5" width="7" height="13" rx="1.3" fill="none" stroke="#5b9fd8" stroke-width="1.5"/>
          <circle cx="13" cy="17.2" r=".9" fill="#5b9fd8"/>
        </svg>
        0455 817 296
      </li>
      <li class="contact">
        <span class="contact-rule"></span>
        <svg class="contact-icon" viewBox="0 0 26 26" aria-hidden="true">
          <circle cx="13" cy="13" r="11.5" fill="#eaf4fc" stroke="#8fc0e8" stroke-width="1.5"/>
          <rect x="7" y="9" width="12" height="8.5" rx="1" fill="#5b9fd8"/>
          <path d="M7.3 9.4 13 14l5.7-4.6" fill="none" stroke="#eaf4fc" stroke-width="1.2"/>
        </svg>
        info@corinvale.example
      </li>
    </ul>
  </section>

</body>
</html>
```